Business Consulting Company requires a website design (PSD+HTML+CSS required)

Tarnvale Advisory is a Business Consulting Company that provides Analysis, Business Coaching and Systems and Document Design for clients.

We would like a simplistic yet professional looking website design that uses high quality imagery to project a professional persona across our entire site.

The completed project will need to include PSD files (for editing in Photoshop) and will need to also include HTML+CSS coded files that can be edited in Adobe Dreamweaver CS5.5.

Tarnvale Advisory currently has a functioning website (located at www.tarnvaleadvisory.com.au) but would like to replace its current site with something more professional, user friendly and content simplistic, with the overall design of this project being clean and very easy to navigate whilst remaining professionally focused.

A brief has been attached to this project to provide the key details but please feel free to contact me if you require any clarification or have any questions regarding the project.

Target Market(s)

The target audience for this website will be small to medium sized businesses (of all descriptions).

Industry/Entity Type

Business

Coding

Coded - Design and coding required

Number of Pages Required

5+ page

Requirements
Must have
• Simplistic design structure
• Professional images
• Easy to navigate
• Must be uploaded in PSD format
• Must be coded (HTML+CSS) and compatible with Adobe Dreamweaver CS5.5
Nice to have
• Use of the Company’s corporate colours throughout the site design
• Adding a Home page slider bar with images and short catchy messages (i.e. text based statements)
• Having a quick link box on each page that provides easy navigation throughout the site
• The use of different icons and images to depict our different services (i.e. a different icon and image for analysis service and coaching service etc.).
• All pages should follow a similar theme (universal approach to all pages)
Should not have
• When coding, images should not be used in place of text (all text must be editable)

```html
<!DOCTYPE html>
<html lang="en">
<head>
<meta charset="utf-8">
<title>Tarnvale Advisory – Home</title>
<link href="https://fonts.googleapis.com/css2?family=Fira+Sans+Extra+Condensed:wght@500;600&family=Fjalla+One&family=Open+Sans:wght@400;600;700&display=swap" rel="stylesheet">
<style>
:root{
  --blue:#1a86cf;
  --blue-dark:#1262a8;
  --blue-band:#1f62ae;
  --heading-blue:#1d5fa8;
  --text:#555;
  --text-dark:#333;
  --topbar:#2f2f2f;
  --footer:#2e2e2e;
  --footer-bottom:#232323;
  --footer-text:#bdbdbd;
  --page:#f1f1f1;
}
*{margin:0;padding:0;box-sizing:border-box}
html,body{width:1112px;height:1200px;overflow:hidden}
body{position:relative;background:var(--page);font-family:"Open Sans",sans-serif;color:var(--text)}
.abs{position:absolute}
.topbar{left:0;top:0;width:1112px;height:30px;background:var(--topbar);color:#bbb;font-size:11px;text-align:right;padding:8px 121px 0 0}
.topbar span{margin:0 8px}
.header{left:0;top:30px;width:1112px;height:79px;background:linear-gradient(#29a3e6,#1578c6)}
.logo-box{left:122px;top:21px;width:213px;height:96px;background:#fff;border:3px solid #e6e6e6;box-shadow:0 2px 4px rgba(0,0,0,.3);display:flex;align-items:center;justify-content:center;gap:8px;z-index:3}
.logo-dot{width:14px;height:14px;border-radius:50%;background:var(--blue)}
.logo-name{font-family:"Open Sans",sans-serif;font-size:17px;font-weight:600;color:#555}
.nav{top:54px;left:447px;display:flex;align-items:center;font-size:14px;font-weight:600;color:#fff;height:28px}
.nav a{color:#fff;text-decoration:none}
.nav .sep{margin:0 14px;opacity:.9}
.nav .current{background:linear-gradient(#fff,#dcdcdc);color:#1a5d9c;padding:4px 16px;border-radius:2px;box-shadow:0 1px 2px rgba(0,0,0,.3)}
.hero{left:0;top:109px;width:1112px;height:341px;background:linear-gradient(180deg,#3b5a80 0%,#8aa4c2 45%,#a79a82 65%,#6a5a44 100%)}
.hero-title{left:740px;top:236px;font-family:"Fjalla One",sans-serif;font-size:52px;color:#fff;text-shadow:0 2px 4px rgba(0,0,0,.4)}
.arrow{width:40px;height:37px;background:linear-gradient(#f4f4f4,#cfcfcf);border-radius:2px;display:flex;align-items:center;justify-content:center}
.services{left:0;top:452px;width:1112px;height:111px;background:#fff}
.service{top:20px;width:160px;text-align:center;font-size:13px;line-height:17px;color:var(--text-dark)}
.service svg{display:block;margin:0 auto 14px}
.intro h1{font-family:"Fira Sans Extra Condensed",sans-serif;font-weight:600;font-size:27px;color:var(--text-dark)}
.intro h1 em{font-style:normal;color:var(--heading-blue)}
.intro p{font-size:12.6px;line-height:23.5px;margin-top:10px;width:580px}
.intro{left:122px;top:588px}
.quote-band{left:0;top:795px;width:1112px;height:89px;background:var(--blue-band);border-top:4px solid #3a86d0}
.quote-band h3{position:absolute;left:122px;top:16px;color:#fff;font-size:12.5px;font-weight:700}
.quote-band p{position:absolute;left:122px;top:38px;width:575px;color:#8fb4e0;font-size:11.6px;line-height:22px}
.sidebar{left:720px;top:412px;width:271px;height:485px;background:#fff;border-top:5px solid #dbe9f5;box-shadow:0 0 6px rgba(0,0,0,.12);z-index:2}
.sidebar h2{font-family:"Fira Sans Extra Condensed",sans-serif;font-weight:600;font-size:27px;color:var(--heading-blue)}
.side-about{padding:16px 20px 0 17px}
.side-about p{font-size:11.5px;line-height:22px;color:#444;margin:10px 0 0 7px}
.side-contact{position:absolute;left:0;top:229px;width:271px;height:251px;background:linear-gradient(#eeeeee,#f7f7f7);padding:14px 0 0 22px}
.field{position:absolute;border:1px solid #bbb;background:#fff;font-size:11px;color:#777;padding:6px 9px}
.submit{position:absolute;left:22px;top:196px;width:226px;height:35px;background:linear-gradient(#2a9fe2,#136fbc);border-radius:3px;color:#fff;font-weight:600;font-size:14.5px;text-align:center;line-height:35px;box-shadow:0 2px 3px rgba(0,0,0,.25)}
.footer{left:0;top:884px;width:1112px;height:253px;background:var(--footer);color:var(--footer-text)}
.foot-logo{left:122px;top:78px;display:flex;align-items:center;gap:9px}
.foot-logo .logo-name{color:#aaa;font-size:20px}
.foot-about{left:122px;top:140px;width:238px;text-align:center;font-size:11.3px;line-height:21px}
.foot-h{font-family:"Open Sans",sans-serif;font-size:26px;color:#d8d8d8;top:50px}
.foot-h::after{content:"";display:block;width:74px;height:3px;background:#aaa;margin-top:7px}
.links{top:110px;display:grid;grid-template-columns:106px 100px;row-gap:10px;font-size:13.5px;list-style:none}
.links li::before{content:"•";font-size:9px;margin-right:14px;vertical-align:2px}
.info{left:741px;top:107px;font-size:13.5px;width:250px}
.info div{display:flex;gap:10px;margin-bottom:14px;line-height:21px}
.info svg{flex:none;margin-top:3px}
.bottombar{left:0;top:1137px;width:1112px;height:63px;background:var(--footer-bottom)}
.copy{left:122px;top:22px;font-size:12.5px;color:#999}
.social{left:885px;top:24px;display:flex;gap:14px}
.social span{width:15px;height:15px;border-radius:50%;background:#2c77c7}
</style>
</head>
<body>
<div class="abs topbar">Email : admin@tarnvaleadvisory.com.au<span>|</span>Phone : 03 5550 0182</div>
<div class="abs header"></div>
<div class="abs logo-box"><span class="logo-dot"></span><span class="logo-name">Tarnvale Advisory</span></div>
<nav class="abs nav">
  <a class="current" href="#">Home</a><span class="sep">I</span>
  <a href="#">About Us</a><span class="sep">I</span>
  <a href="#">Services</a><span class="sep">I</span>
  <a href="#">Contact Us</a><span class="sep">I</span>
  <a href="#">Testimonials</a>
</nav>

<div class="abs hero" role="img" aria-label="Slider photo: an elephant walking down a country road at dusk under a wide sky"></div>
<div class="abs hero-title">Build Strong</div>
<div class="abs arrow" style="left:37px;top:242px"><svg width="12" height="14" viewBox="0 0 12 14"><path d="M9 1 3 7l6 6" fill="none" stroke="#444" stroke-width="3"/></svg></div>
<div class="abs arrow" style="left:1035px;top:242px"><svg width="12" height="14" viewBox="0 0 12 14"><path d="M3 1l6 6-6 6" fill="none" stroke="#444" stroke-width="3"/></svg></div>

<section class="abs services">
  <div class="abs service" style="left:91px">
    <svg width="36" height="36" viewBox="0 0 36 36"><g fill="#243b5e"><rect x="2" y="24" width="4" height="10"/><rect x="8" y="22" width="4" height="12"/><rect x="14" y="20" width="4" height="14"/><rect x="20" y="17" width="4" height="17"/><rect x="26" y="14" width="4" height="20"/></g><path d="M3 20 Q20 18 30 4" fill="none" stroke="#1a86cf" stroke-width="3"/><path d="M24 4h9v9z" fill="#1a86cf"/></svg>
    In house<br>business analysis</div>
  <div class="abs service" style="left:242px">
    <svg width="36" height="36" viewBox="0 0 36 36"><rect x="13" y="3" width="20" height="22" fill="none" stroke="#243b5e" stroke-width="2"/><circle cx="7" cy="6" r="3.5" fill="#1a86cf"/><rect x="3" y="11" width="8" height="12" fill="#1a86cf"/><rect x="4" y="23" width="2.5" height="11" fill="#1a86cf"/><rect x="7.5" y="23" width="2.5" height="11" fill="#1a86cf"/><path d="M11 13l6-3" stroke="#1a86cf" stroke-width="2"/><path d="M19 33l4-5 4 5" fill="none" stroke="#243b5e" stroke-width="2"/></svg>
    Individual<br>business coaching</div>
  <div class="abs service" style="left:399px">
    <svg width="36" height="36" viewBox="0 0 36 36"><path d="M4 2h18l8 8v24H4z" fill="none" stroke="#243b5e" stroke-width="2"/><path d="M22 2v8h8" fill="none" stroke="#243b5e" stroke-width="2"/><rect x="12" y="16" width="22" height="11" fill="#1a86cf"/><rect x="15" y="20" width="16" height="3" fill="#fff"/></svg>
    Business systems<br>&amp; document creation</div>
  <div class="abs service" style="left:555px">
    <svg width="36" height="36" viewBox="0 0 36 36"><path d="M12 8V4h12v4" fill="none" stroke="#243b5e" stroke-width="3"/><rect x="1" y="8" width="34" height="24" rx="5" fill="#1a86cf"/><path d="M1 18h34" stroke="#fff" stroke-width="2"/><rect x="15" y="15" width="6" height="7" rx="1" fill="#243b5e"/></svg>
    New business<br>start up packages</div>
</section>

<section class="abs intro">
  <h1><em>Making Business As</em> Easy As Child’s Play!</h1>
  <p>Tarnvale Advisory is a Business Development and Consulting Company that provides affordable, high quality business solutions that are easy to understand and that are individually tailored to suit the needs of our clients.</p>
  <p style="margin-top:6px">Understanding that each of our clients businesses are unique, Tarnvale works closely with our business partners to ensure the correct solutions are in place and that optimum efficiency is achieved.</p>
</section>

<section class="abs quote-band">
  <h3>Dana Whitfield - Director Kestrel Fields Pty Ltd.</h3>
  <p>Kestrel Fields recently engaged Tarnvale Advisory to assist with the immediate needs and the future development of our business. At first I was a little sceptical as to what, if anything, Tarnvale ...</p>
</section>

<aside class="abs sidebar">
  <div class="side-about">
    <h2>About Us</h2>
    <p>Lorem Ipsum is simply dummy text of the printing and typesetting industry. Lorem Ipsum has been the industry's standard dummy text ever since the 1500s, when an unknown printer took a galley of type and scrambled it to make a type specimen book.</p>
  </div>
  <div class="side-contact">
    <h2>Contact Us</h2>
    <div class="field" style="left:22px;top:73px;width:123px;height:27px">Fist name</div>
    <div class="field" style="left:22px;top:112px;width:123px;height:27px">Email</div>
    <div class="field" style="left:22px;top:151px;width:123px;height:27px">+91</div>
    <div class="field" style="left:141px;top:73px;width:107px;height:105px">Massage</div>
    <div class="submit">Submit Enquiry Now</div>
  </div>
</aside>

<footer class="abs footer">
  <div class="abs foot-logo"><span class="logo-dot"></span><span class="logo-name">Tarnvale Advisory</span></div>
  <p class="abs foot-about">when an unknown printer took a galley of type and scrambled it to make a type specimen book.</p>
  <h2 class="abs foot-h" style="left:454px">Quick Link</h2>
  <ul class="abs links" style="left:454px">
    <li>About Us</li><li>Business</li>
    <li>Services</li><li>Packages</li>
    <li>Coaching</li><li>Templates</li>
    <li>Analysis</li><li>Contact Us</li>
  </ul>
  <h2 class="abs foot-h" style="left:741px">Contact Info</h2>
  <div class="abs info">
    <div><svg width="14" height="18" viewBox="0 0 14 18"><path d="M7 0a7 7 0 0 0-7 7c0 5 7 11 7 11s7-6 7-11a7 7 0 0 0-7-7z" fill="#fff"/><circle cx="7" cy="7" r="2.5" fill="#2e2e2e"/></svg><span>PO Box: 4127, Moorfield, Victoria, Australia 3899</span></div>
    <div><svg width="14" height="16" viewBox="0 0 14 16"><path d="M3 0l3 4-2 2c1 3 3 5 5 6l2-2 3 3-2 3C6 15 0 9 0 3z" fill="#fff"/></svg><span>03 5550 0182</span></div>
    <div><svg width="14" height="12" viewBox="0 0 14 12"><rect y="1" width="14" height="10" fill="#fff"/><path d="M0 1l7 5 7-5" fill="none" stroke="#2e2e2e" stroke-width="1.5"/></svg><span>admin@tarnvaleadvisory.com.au</span></div>
  </div>
</footer>
<div class="abs bottombar">
  <p class="abs copy">Copyright © 2014 Tarnvale Advisory. All Rights Reserved.</p>
  <div class="abs social"><span></span><span></span><span></span><span></span></div>
</div>
</body>
</html>
```